Lintel Systems

Looking for a web site design to market our services/applications
We write and supply bespoke web applications for the offshore and construction industries
Our initial product is Volk - rope access equipment management
Our buyers will be Rope Access companies via trade associations such as KEFOB and GLUMP
we have a logo designed see it attached we would like to see crisp professional designs based around these colours and design
we will supply web copy later
looking for home, services, blog, contact us, order and a general template (privacy, site map, T&C) pages
Updates
This payment will be for the homepage only
We can discuss other options (pages) with the successful designer
Regards
Norman
Industry/Entity Type
Construction
Look and feel

```html
<!DOCTYPE html>
<html lang="en">
<head>
<meta charset="utf-8">
<title>Lintel Systems</title>
<link rel="stylesheet" href="https://fonts.googleapis.com/css2?family=Open+Sans:wght@400;600&family=Arimo:wght@400;700&display=swap">
<style>
:root{
  --blue:#0a90d3;
  --navy:#0d2a8a;
  --text:#333;
  --muted:#8a8a8a;
  --dark:#222;
  --footer:#333333;
  --footer-bottom:#2b2b2b;
  --white:#fff;
}
*{box-sizing:border-box;margin:0;padding:0}
html,body{width:1091px;height:1200px;overflow:hidden;background:var(--white)}
body{position:relative;font-family:"Open Sans",sans-serif;color:var(--text)}
.abs{position:absolute}
.logo{left:129px;top:26px;display:flex;align-items:center;gap:12px}
.logo-mark{width:48px;height:48px;background:var(--navy);border-radius:6px}
.logo-rule{width:1px;height:70px;background:#dcdcdc}
.logo-name{font-weight:600;font-size:21px;color:var(--navy);line-height:1}
.member{left:858px;top:52px;width:106px;height:29px;background:var(--navy);color:var(--white);font-size:11px;font-weight:600;display:flex;align-items:center;justify-content:center;border-radius:2px}
.nav{left:129px;top:125px;width:835px;height:43px;background:linear-gradient(#3a3a3a,#000);border-radius:5px 5px 0 0;border-bottom:2px solid var(--blue);display:flex;align-items:center;overflow:hidden}
.nav a{color:var(--white);text-decoration:none;font-size:13.5px;letter-spacing:.3px}
.nav .home{background:var(--blue);height:100%;width:91px;display:flex;align-items:center;justify-content:center}
.nav .item{position:absolute}
.hero{left:129px;top:168px;width:835px;height:339px;background:linear-gradient(110deg,#5f7698 0%,#b6c6dc 35%,#e8edf3 55%,#a9bad0 80%,#6c7f9c 100%)}
.hero-arrow{top:314px;width:26px;height:27px;background:#000;display:flex;align-items:center;justify-content:center}
.mini{top:525px;width:15px;height:15px;border-radius:50%;background:#9a9a9a;display:flex;align-items:center;justify-content:center}
.feature{top:550px;width:280px;height:92px}
.feature-icon{position:absolute;left:0;top:4px;width:85px;height:85px;border-radius:50%;background:#f4f4f4;box-shadow:0 1px 4px rgba(0,0,0,.25);display:flex;align-items:center;justify-content:center}
.feature-icon .disc{width:72px;height:72px;border-radius:50%;background:radial-gradient(circle at 45% 40%,#3aaee6,#0a7fc0);display:flex;align-items:center;justify-content:center}
.feature-rule{position:absolute;left:93px;top:0;width:1px;height:96px;background:#e2e2e2}
.feature h3{position:absolute;left:102px;top:2px;font-weight:400;font-size:18px;color:#555}
.feature p{position:absolute;left:102px;top:32px;width:165px;font-size:10.5px;line-height:14.5px;color:var(--muted)}
.divider{left:129px;top:666px;width:835px;height:12px;background:radial-gradient(ellipse at top,rgba(0,0,0,.12),rgba(0,0,0,0) 70%)}
.welcome{left:129px;top:704px;font-size:17.5px;font-weight:600;color:var(--navy)}
.photo{left:128px;top:757px;width:206px;height:191px;border:1px solid #ddd;padding:4px;background:var(--white)}
.photo div{width:100%;height:100%;background:linear-gradient(100deg,#e9e4dd 0%,#d9c7b0 40%,#f2f0ec 65%,#7b8595 100%)}
.sub{left:343px;top:757px;font-size:12.5px;font-weight:600;color:#1c5a96}
.body-text{left:343px;width:338px;font-size:10.2px;line-height:15.4px;color:var(--text);text-align:justify}
.form{left:707px;top:708px;width:256px;height:245px;background:var(--dark);border-bottom:4px solid var(--blue)}
.form h2{height:34px;background:var(--blue);color:var(--white);font-weight:400;font-size:17px;padding:4px 9px}
.form label{position:absolute;left:9px;color:var(--white);font-family:"Arimo",sans-serif;font-size:10.5px}
.form .field{position:absolute;left:72px;width:170px;height:26px;background:var(--white)}
.form .submit{position:absolute;left:158px;top:206px;width:84px;height:25px;background:var(--blue);color:var(--white);font-size:13.5px;display:flex;align-items:center;justify-content:center}
.footer{left:0;top:983px;width:1091px;height:177px;background:var(--footer)}
.footer-bottom{left:0;top:1160px;width:1091px;height:40px;background:var(--footer-bottom);border-top:1px solid #444;color:#ddd;font-family:"Arimo",sans-serif;font-size:10px;display:flex;align-items:center;justify-content:center}
.links{list-style:none;font-family:"Arimo",sans-serif;font-size:10.4px;color:#eee}
.links li{height:25.6px}
.news-title{left:555px;top:1000px;color:var(--white);font-size:13.5px;font-weight:400}
.news-input{left:553px;width:179px;height:28px;background:var(--white);font-family:"Arimo",sans-serif;font-size:10px;color:#444;padding:7px 6px}
.signup{left:653px;top:1113px;width:79px;height:28px;background:var(--blue);color:var(--white);font-size:13.5px;display:flex;align-items:center;justify-content:center}
.partner{top:1018px;height:40px;display:flex;align-items:center;justify-content:center;font-family:"Arimo",sans-serif;font-weight:700;font-size:15px;color:#e8e8e8}
.partner-oval{left:802px;width:72px;border-radius:50%;background:#e8e8e8;color:#333}
.partner-plain{left:882px;width:80px}
.social{top:1082px;width:25px;height:25px;border-radius:50%}
</style>
</head>
<body>

<div class="abs logo">
  <div class="logo-mark"></div>
  <div class="logo-rule"></div>
  <div class="logo-name">Lintel Systems</div>
</div>
<div class="abs member">SUPER - MEMBER</div>

<nav class="abs nav">
  <a class="home" href="#">HOME</a>
  <a class="item" href="#" style="left:193px">SERVICES</a>
  <a class="item" href="#" style="left:383px">BLOG</a>
  <a class="item" href="#" style="left:550px">ORDER</a>
  <a class="item" href="#" style="left:726px">CONTACT US</a>
</nav>

<div class="abs hero" role="img" aria-label="Two engineers in hard hats reviewing plans in front of office towers"></div>
<div class="abs hero-arrow" style="left:129px"><svg width="8" height="12" viewBox="0 0 8 12"><path d="M6 1L1 6l5 5" stroke="#fff" stroke-width="2" fill="none"/></svg></div>
<div class="abs hero-arrow" style="left:938px"><svg width="8" height="12" viewBox="0 0 8 12"><path d="M2 1l5 5-5 5" stroke="#fff" stroke-width="2" fill="none"/></svg></div>

<div class="abs mini" style="left:930px"><svg width="6" height="8" viewBox="0 0 6 8"><path d="M4.5 1L1.5 4l3 3" stroke="#fff" stroke-width="1.5" fill="none"/></svg></div>
<div class="abs mini" style="left:949px"><svg width="6" height="8" viewBox="0 0 6 8"><path d="M1.5 1l3 3-3 3" stroke="#fff" stroke-width="1.5" fill="none"/></svg></div>

<section class="abs feature" style="left:129px">
  <div class="feature-icon"><div class="disc">
    <svg width="34" height="40" viewBox="0 0 34 40" aria-label="Phone icon" role="img"><rect x="8" y="2" width="18" height="36" rx="3" fill="none" stroke="#fff" stroke-width="2.5"/><rect x="11" y="7" width="12" height="22" fill="#fff" opacity=".85"/><circle cx="17" cy="33" r="1.8" fill="#fff"/></svg>
  </div></div>
  <div class="feature-rule"></div>
  <h3>Record</h3>
  <p>Sed ut perspiciatis unde omnis iste natus error sit voluptatem accusantium doloremque lau-dantium, totam rem aperiam,</p>
</section>
<section class="abs feature" style="left:415px">
  <div class="feature-icon"><div class="disc">
    <svg width="34" height="40" viewBox="0 0 34 40" aria-label="Light bulb icon" role="img"><path d="M17 3a11 11 0 0 0-6 20v5h12v-5A11 11 0 0 0 17 3z" fill="#ffd23a" stroke="#fff" stroke-width="2"/><rect x="12" y="30" width="10" height="3" fill="#fff"/><rect x="13" y="35" width="8" height="3" rx="1" fill="#fff"/></svg>
  </div></div>
  <div class="feature-rule"></div>
  <h3>Tools</h3>
  <p>Sed ut perspiciatis unde omnis iste natus error sit voluptatem accusantium doloremque lau-dantium, totam rem aperiam,</p>
</section>
<section class="abs feature" style="left:700px">
  <div class="feature-icon"><div class="disc">
    <svg width="40" height="36" viewBox="0 0 40 36" aria-label="Rising bar chart icon" role="img"><rect x="3" y="24" width="6" height="10" fill="#fff"/><rect x="12" y="18" width="6" height="16" fill="#fff"/><rect x="21" y="13" width="6" height="21" fill="#fff"/><rect x="30" y="7" width="6" height="27" fill="#fff"/><path d="M3 18l10-7 7 4 14-12" stroke="#ff5a3c" stroke-width="2.5" fill="none"/><path d="M28 3h6v6" stroke="#ff5a3c" stroke-width="2.5" fill="none"/></svg>
  </div></div>
  <div class="feature-rule"></div>
  <h3>Goals</h3>
  <p>Sed ut perspiciatis unde omnis iste natus error sit voluptatem accusantium doloremque lau-dantium, totam rem aperiam,</p>
</section>

<div class="abs divider"></div>

<h1 class="abs welcome">Welcome to Our Company !</h1>
<div class="abs photo"><div role="img" aria-label="Smiling businesswoman in a white shirt in an office"></div></div>
<div class="abs sub">Website of Harbour Mutual Finance Co-operative.</div>
<p class="abs body-text" style="top:794px">Lorem ipsum dolor sit amet, consectetur adipisicing elit, sed do eius-mod tempor incididunt ut labore et dolore magna aliqua. Ut enim ad minim veniam, quis nostrud exercitation ullamco laboris nisi ut aliquip ex ea commodo dolore eu fugiat nulla pariatur. Excepteur sint occae-cat cupidatat non proident, sunt in culpa qui officia deserunt mollit anim id est laborum</p>
<p class="abs body-text" style="top:902px">Lorem ipsum dolor sit amet, consectetur adipisicing elit, sed do eius-mod tempor incididunt ut labore et dolore magna aliqua. Ut enim ad deams a reality.</p>

<form class="abs form">
  <h2>Contact Form</h2>
  <label style="top:51px">Name</label><div class="field" style="top:44px"></div>
  <label style="top:86px">Email</label><div class="field" style="top:78px"></div>
  <label style="top:121px">Phone:</label><div class="field" style="top:112px"></div>
  <label style="top:156px">Comments</label><div class="field" style="top:147px;height:48px"></div>
  <div class="submit">SUBMIT</div>
</form>

<footer class="abs footer"></footer>
<ul class="abs links" style="left:130px;top:1002px"><li>Home</li><li>About</li><li>News</li><li>Services</li><li>What We Do</li><li>Contact Us</li></ul>
<ul class="abs links" style="left:253px;top:1002px"><li>Grief &amp; Healing</li><li>Resources</li><li>Plan Now</li><li>Locations</li><li>Privacy Policy</li><li>Terms &amp; Conditions</li></ul>
<ul class="abs links" style="left:402px;top:1002px"><li>Privacy</li><li>Sitemap</li><li>T&amp;C</li></ul>

<h4 class="abs news-title">NEWSLETTER SIGN UP</h4>
<div class="abs news-input" style="top:1032px">Enter Name</div>
<div class="abs news-input" style="top:1071px">Enter Email Address</div>
<div class="abs signup">SIGN UP</div>

<div class="abs partner partner-oval">KEFOB</div>
<div class="abs partner partner-plain">GLUMP</div>

<div class="abs social" style="left:807px;background:#3b5b9b"></div>
<div class="abs social" style="left:838px;background:#22a7e0"></div>
<div class="abs social" style="left:869px;background:#1a73b3"></div>
<div class="abs social" style="left:900px;background:#e0382c"></div>
<div class="abs social" style="left:931px;background:#f36f21"></div>

<div class="abs footer-bottom">© Copyright&nbsp; 2014 Lintel Systems All right recived</div>

</body>
</html>
```